www.brightwhelk.com.au

I am looking to create a brochure (fold out) for each of the 7 Brightwhelk Properties and a new ‘group’ Brochure. I am looking for a fresh theme, with the following components:
· Brightwhelk Logo (top Left)
· Kindle Camps Logo (Top Right)
· Location Band immediately beneath the two logos
· Contact details bottom of brochure
· Map on Back of Brochure

I would like to keep the brochures friendly and family orientated with clear information.

I would like to start with Orrin Meadows Caravan Park and once chosen the design negotiate to do the remaining properties.

Target Market(s)

Older travellers, young families, couples

Industry/Entity Type

Group

Font styles to use
Serif

Colors
85cae6
3377b5
0293ce
cedeed
cfe9f5
89d0c7
86cfc6

Requirements
Must have
• Be a fold out DL sized brochure
• · Brightwhelk Logo (top Left)
• · Kindle Camps Logo (Top Right)
• · Location Band immediately beneath the two logos
• · Contact details
• · Map on Back of Brochure
• Map of where other Brightwhelk Properties are with Brightwhelk website

```html
<!DOCTYPE html>
<html lang="en">
<head>
<meta charset="utf-8">
<title>Orrin Meadows Caravan Park – Inside Spread</title>
<link href="https://fonts.googleapis.com/css2?family=Bitter:wght@400;600;700&family=Roboto+Condensed:wght@400;500&display=swap" rel="stylesheet">
<style>
:root{
  --navy:#1c4270;
  --panel-navy:#0f4d7e;
  --teal:#45bfcb;
  --teal-soft:#85cae6;
  --text-teal:#2ba6c9;
  --white:#ffffff;
  --tour-red:#e5563b;
  --trail-orange:#f1a935;
  --water-green:#2aa58c;
  --arts-pink:#e8659f;
  --events-blue:#1776bb;
  --serif:'Bitter', Georgia, serif;
  --sans:'Roboto Condensed', Arial, sans-serif;
}
html,body{margin:0;padding:0;overflow:hidden;}
body{width:1200px;height:851px;background:var(--white);}
.brochure{position:relative;width:1200px;height:851px;overflow:hidden;font-family:var(--sans);}
.backdrop{position:absolute;left:0;top:0;}
.panel-title{position:absolute;top:60px;font-family:var(--serif);font-weight:600;font-size:26px;color:var(--navy);margin:0;}
.intro{position:absolute;font-family:var(--serif);font-weight:600;color:var(--navy);margin:0;}
.photo{position:absolute;box-sizing:border-box;}
.accom-photo{left:16px;width:175px;height:105px;border:2px solid var(--panel-navy);}
.accom-info{position:absolute;left:199px;width:190px;}
.accom-info h3{font-family:var(--serif);font-weight:600;font-size:12.5px;color:var(--navy);margin:0 0 5px;}
.accom-info p{font-size:9.4px;line-height:8.6px;color:var(--text-teal);margin:0 0 8px;}
.facility-photo{border:2px solid var(--panel-navy);}
.facility-box{position:absolute;background:var(--panel-navy);color:var(--white);font-size:13.5px;line-height:15.5px;box-sizing:border-box;padding:10px 10px 10px 12px;}
.facility-box p{margin:0 0 16px;}
.facility-box p:last-child{margin:0;}
.town-name{position:absolute;left:822px;top:196px;width:100px;display:flex;flex-direction:column;align-items:flex-start;gap:6px;font-family:var(--serif);font-weight:700;font-size:16px;line-height:18px;color:var(--navy);}
.town-name .mark{width:14px;height:14px;background:var(--teal);}
.town-intro{position:absolute;left:933px;top:184px;width:200px;font-size:11.3px;line-height:15.5px;color:var(--text-teal);margin:0;}
.whats-box{position:absolute;box-sizing:border-box;color:var(--white);font-size:11.2px;line-height:15.5px;padding:9px 10px;display:flex;align-items:center;}
.whats-box.right-align{text-align:right;justify-content:flex-end;}
.whats-photo{border:2px solid;}
.whats-photo span{position:absolute;left:0;right:0;font-family:var(--serif);font-weight:600;color:var(--white);text-align:center;text-shadow:0 1px 3px rgba(0,0,0,.6);line-height:23px;}
</style>
</head>
<body>
<div class="brochure">

  <svg class="backdrop" width="1200" height="851" viewBox="0 0 1200 851">
    <defs>
      <linearGradient id="sky" x1="0" y1="0" x2="0" y2="1">
        <stop offset="0" stop-color="#3fbecb"/>
        <stop offset="1" stop-color="#8fd8e0"/>
      </linearGradient>
    </defs>
    <rect width="1200" height="240" fill="url(#sky)" role="img" aria-label="Teal sunburst rays radiating from the top of the spread"/>
    <rect x="401" y="96" width="401" height="755" fill="var(--teal)"/>
    <rect x="802" y="98" width="398" height="753" fill="var(--white)"/>
    <path d="M0,62 C300,44 900,44 1200,58 L1200,100 L802,100 C700,94 500,94 401,98 C250,100 120,102 0,112 Z" fill="var(--white)"/>
    <path d="M0,225 C120,150 260,108 401,98 L401,851 L0,851 Z" fill="var(--white)"/>
  </svg>

  <!-- Accommodation -->
  <h2 class="panel-title" style="left:93px;">Accommodation</h2>
  <p class="intro" style="right:812px;top:128px;width:300px;text-align:right;font-size:14.5px;line-height:14.3px;">
    Vivamus aliquet elit sem,<br>et ornare ex aliquam in.<br>In cursus, felis non pretium<br>molestie, tellus lacus facilisis<br>metus, ut accumsan<br>nisi nulla accumsan rius.
  </p>

  <div class="photo accom-photo" style="top:236px;background:linear-gradient(#8cc4ea 0 45%,#efe9d8 45% 80%,#8a9a6c 80%);" role="img" aria-label="Holiday spa unit cabin with veranda under blue sky"></div>
  <div class="accom-info" style="top:241px;">
    <h3>Holiday Spa unit</h3>
    <p>Two bedroom unit with a queen size bed and two single beds complete with all linen.</p>
    <p>Living area, kitchen /dining and lounge area.</p>
    <p>The bathroom has a two person spa, and separate shower recess.</p>
    <p>This is a non smoking unit.</p>
  </div>

  <div class="photo accom-photo" style="top:354px;background:linear-gradient(#a9cbe6 0 40%,#f2f0ec 40% 75%,#2d5c8c 75%);" role="img" aria-label="1-2 bedroom holiday unit with blue trimmed deck"></div>
  <div class="accom-info" style="top:359px;">
    <h3>1-2 Bedroom Holiday unit</h3>
    <p>Similar size to the spa unit and is fully self-contained.</p>
    <p>Two bedroom unit with a queen size bed and two single beds complete with all linen.</p>
    <p>Living area, kitchen /dining and lounge area.</p>
    <p>This is a non smoking unit.</p>
  </div>

  <div class="photo accom-photo" style="top:470px;background:linear-gradient(#9ec3e0 0 30%,#c9b28f 30% 70%,#4f5a3e 70%);" role="img" aria-label="Brick cottages beside a tree-lined driveway"></div>
  <div class="accom-info" style="top:475px;">
    <h3>1-2 Bedroom Cottages</h3>
    <p>This unit is constructed of brick has two bedrooms and is fully self contained.</p>
    <p>Two bedroom unit with a queen size bed and two single beds complete with all linen.</p>
    <p>Living area, kitchen /dining and lounge area.</p>
    <p>This is a non smoking unit.</p>
  </div>

  <div class="photo accom-photo" style="top:586px;background:linear-gradient(#9fc9ea 0 35%,#ede7d6 35% 85%,#b9b1a0 85%);" role="img" aria-label="Cream weatherboard studio chalet"></div>
  <div class="accom-info" style="top:592px;">
    <h3>Studio &amp; 2-Bedroom Chalets</h3>
    <p>The studio chalet is an older style unit pleasantly presented. It is fully self contained.</p>
    <p>The sleeping arrangements are two sets of bunk beds separated by a curtain from the main living area, in the living area is a queen size bed complete with all linen.</p>
    <p>This is a non smoking unit.</p>
  </div>

  <div class="photo accom-photo" style="top:704px;background:linear-gradient(#b7cfe0 0 35%,#8a9a7a 35% 60%,#e6e4df 60% 85%,#9a8c74 85%);" role="img" aria-label="Caravan parked on a shady powered site"></div>
  <div class="accom-info" style="top:708px;">
    <h3>Powered Sites</h3>
    <p>Large, Shady or Open Powered Caravan Sites for up to 24-foot caravan &amp; motorhomes. Larger Vans or Buses can be accommodated upon request.</p>
    <p>Close by are camper's kitchen, guest laundry and children's playground.</p>
    <p>Parking for one vehicle with site.</p>
  </div>

  <!-- Facilities -->
  <h2 class="panel-title" style="left:550px;">Facilities</h2>
  <p class="intro" style="left:425px;top:145px;width:360px;text-align:center;font-size:14px;line-height:14.5px;">
    Pellentesque sit amet tristique elit. Aliquam semper ultricies nulla nec molestie. Nulla facilisi. Cum sociis natoque penatibus et magnis dis parturient montes, nascetur ridiculus mus.
  </p>

  <div class="facility-box" style="left:594px;top:242px;width:196px;height:101px;">
    <p>Swimming Pool</p>
    <p>Television room with large wide screen TV, pool table and table tennis</p>
  </div>
  <div class="photo facility-photo" style="left:426px;top:235px;width:170px;height:114px;background:linear-gradient(#2f6fa8 0 35%,#c9c4b2 35% 55%,#3fb6e0 55% 85%,#d8d4c8 85%);" role="img" aria-label="Swimming pool under blue shade sail"></div>

  <div class="facility-box" style="left:540px;top:391px;width:226px;height:132px;">
    <p>Large Jumping Pillow with adjoining playground to entertain the kids</p>
    <p>Large entrance parking area</p>
    <p>Kiosk with large range of items</p>
  </div>
  <div class="photo facility-photo" style="left:427px;top:374px;width:115px;height:170px;background:linear-gradient(#8fb9e2 0 45%,#cfc9b8 45% 60%,#3fa68c 60%);" role="img" aria-label="Green jumping pillow beside a playground"></div>

  <div class="facility-box" style="left:594px;top:567px;width:188px;height:104px;">
    <p>Campers Kitchen with fridge, cook-tops, microwave, kettle and toaster.</p>
    <p>Large barbeque area.</p>
  </div>
  <div class="photo facility-photo" style="left:426px;top:561px;width:170px;height:116px;background:linear-gradient(#f2f2f0 0 25%,#c9c6c0 25% 70%,#7a5a44 70% 85%,#b0aca6 85%);" role="img" aria-label="Campers kitchen with tables and barbeque"></div>

  <div class="facility-box" style="left:594px;top:702px;width:188px;height:103px;padding-top:24px;">
    <p>Two Laundries (3 washing machines and a dryer in each)</p>
    <p>Large clothes drying areas</p>
  </div>
  <div class="photo facility-photo" style="left:426px;top:696px;width:170px;height:114px;background:linear-gradient(#a9c9e6 0 40%,#9aa0a2 40% 75%,#b87a84 75%);" role="img" aria-label="Laundry building with garden bed"></div>

  <!-- What's on -->
  <h2 class="panel-title" style="left:965px;">What’s on</h2>
  <div class="town-name"><span class="mark"></span>CARROWBY</div>
  <p class="town-intro">The City of Greater Carrowby has a population over 41,000 and includes Fennick, Hollowmere and Tarrenby. From coastline to inland there is a huge variety of things to see and do.</p>

  <div class="whats-box right-align" style="left:814px;top:289px;width:188px;height:94px;background:var(--tour-red);">One of the best ways to explore Carrowby and the Sunward Coast is to go on a tour. Talk to our friendly staff and they will find the tour that is right for you.</div>
  <div class="photo whats-photo" style="left:1000px;top:282px;width:177px;height:106px;border-color:var(--tour-red);background:linear-gradient(#bfc9d1,#8d8a82);" role="img" aria-label="Sea lion resting on the sand"><span style="top:12px;font-size:21px;">TOURS</span></div>

  <div class="photo whats-photo" style="left:814px;top:394px;width:176px;height:107px;border-color:var(--trail-orange);background:linear-gradient(#2f7fd0 0 35%,#6c9a3e 35% 50%,#f1d21f 50%);" role="img" aria-label="Field of yellow wildflowers under blue sky"><span style="top:11px;font-size:21px;">TRAILS &amp;<br>WILDFLOWERS</span></div>
  <div class="whats-box" style="left:988px;top:401px;width:189px;height:94px;background:var(--trail-orange);">With plenty of trails to explore in walking distance to Orrin Meadows Caravan Park, you will have to keep an eye out to spot more than 12,000 species of wildflowers</div>

  <div class="whats-box right-align" style="left:814px;top:515px;width:188px;height:94px;background:var(--water-green);">This family friendly beach also offers barbeques and a playground. Carrowby offers guests a number of unique aquatic experiences.</div>
  <div class="photo whats-photo" style="left:1000px;top:507px;width:177px;height:106px;border-color:var(--water-green);background:linear-gradient(#1b5f9a,#2f86c4 60%,#e4f1f8);" role="img" aria-label="Kite surfer riding a breaking wave"><span style="top:9px;font-size:21px;">JUST ADD<br>WATER</span></div>

  <div class="photo whats-photo" style="left:814px;top:619px;width:176px;height:107px;border-color:var(--arts-pink);background:linear-gradient(#e6a15a,#4a6f92 60%,#2b3e58);" role="img" aria-label="Mosaic public artwork by the water at sunset"><span style="top:8px;font-size:17px;line-height:19px;">ARTS, CULTURE<br>&amp; ENTERTAINMENT</span></div>
  <div class="whats-box" style="left:988px;top:626px;width:189px;height:93px;background:var(--arts-pink);">The Harbourlight Theatre and a vast collection of public art just around the corner from Orrin Meadows Caravan Park.</div>

  <div class="whats-box right-align" style="left:814px;top:737px;width:188px;height:95px;background:var(--events-blue);">Carrowby is the West Coast’s premiere country town, there is always something on showcasing the best in Entertainment.</div>
  <div class="photo whats-photo" style="left:1000px;top:729px;width:177px;height:107px;border-color:var(--events-blue);background:linear-gradient(#1c2f52,#4b5f86 55%,#d89a4a 70%,#1c2a40);" role="img" aria-label="Waterfront building lit at dusk"><span style="top:12px;font-size:19px;">EVENTS</span></div>

</div>
</body>
</html>
```